Flier advertising books and newsletter

A4 flier advertising my free e-newsletter and two books, as well as an invite to like us on quirlo.

needs to look good in full colour but that can be printed in black and white on the occasions that mass mail outs are required and cost becomes an issue.

Modern, funky but acceptable to corporate. No stock photos of people please.

I have attached the file - there are three pictures - one of each book , and also our logo I can attach the original jpegs when required.

UPDATE: The first couple of designs convinced me that there was too much text in my flier for an a4 document so I have edited the attached document to reduce the amount of text.

```html
<!DOCTYPE html>
<html lang="en">
<head>
<meta charset="utf-8">
<title>Bright Paths – Flier</title>
<link href="https://fonts.googleapis.com/css2?family=Arimo:wght@400;700&display=swap" rel="stylesheet">
<style>
  :root {
    --page: #ffffff;
    --edge: #d9dcc8;
    --green: #4d7a10;
    --olive-text: #6a5a12;
    --panel: #5c6c15;
    --ink: #2b2b2b;
    --white: #ffffff;
  }
  * { box-sizing: border-box; margin: 0; padding: 0; }
  html, body { width: 849px; height: 1200px; overflow: hidden; background: var(--page); }
  body { font-family: "Arimo", Arial, sans-serif; color: var(--ink); position: relative; }
  .flier { position: absolute; inset: 0; border: 1px solid var(--edge); }

  .brand { position: absolute; top: 54px; left: 596px; display: flex; align-items: center; gap: 8px; }
  .brand-mark { width: 26px; height: 26px; border-radius: 50%; background: var(--green); }
  .brand-name { color: var(--green); font-weight: 700; font-size: 12px; line-height: 1.15; text-transform: uppercase; letter-spacing: .3px; }
  .brand-name small { display: block; font-size: 7px; text-transform: none; letter-spacing: 0; font-weight: 700; }

  .headline { position: absolute; top: 106px; right: 58px; width: 720px; text-align: right;
    color: var(--green); font-size: 44px; line-height: 1.2; font-weight: 700; letter-spacing: -.5px; }
  .headline .soft { font-weight: 400; }

  .subhead { position: absolute; top: 264px; left: 55px; width: 700px; color: var(--olive-text);
    font-size: 21px; line-height: 1.25; font-weight: 700; }

  .intro { position: absolute; top: 330px; left: 55px; width: 730px; font-size: 13px; line-height: 1.3; }
  .intro .indent { text-indent: 38px; }
  .intro .quote { text-indent: 38px; margin-top: 15px; }
  .intro strong { font-weight: 700; }

  .panel { position: absolute; left: 50px; width: 751px; background: var(--panel); border-radius: 16px; color: var(--white); }
  .panel-book { top: 490px; height: 332px; }
  .panel-senior { top: 838px; height: 314px; }

  .cover { position: absolute; }
  .cover-life { left: 18px; top: 18px; width: 170px; height: 296px;
    background: linear-gradient(180deg, #ffffff 0%, #f3f3f0 45%, #f2d23a 70%, #3a8fd6 100%); }
  .cover-years { left: 540px; top: 18px; width: 184px; height: 278px;
    background: linear-gradient(160deg, #1d3f73 0%, #264c86 50%, #18305a 100%); }

  .panel-book .copy { position: absolute; left: 209px; top: 16px; width: 520px; font-size: 13px; line-height: 1.28; }
  .panel-book h2 { font-size: 20px; font-weight: 700; margin-bottom: 10px; }
  .panel-book .lead { margin-bottom: 14px; }
  .panel-book .ps { font-size: 10.5px; margin-top: 12px; }

  .panel-senior .copy { position: absolute; left: 17px; top: 16px; width: 505px; font-size: 12.5px; line-height: 1.25; }
  .panel-senior h2 { font-size: 21px; line-height: 1.22; font-weight: 700; margin-bottom: 12px; }
  .panel-senior .avail { margin-top: 12px; }
</style>
</head>
<body>
<div class="flier">

  <div class="brand">
    <span class="brand-mark"></span>
    <span class="brand-name">Bright Paths<small>PSYCHOLOGY AND EDUCATION</small><small>helping kids and young people thrive every day</small></span>
  </div>

  <h1 class="headline">Want some <span class="soft">extra help</span> in supporting teens and young people?</h1>

  <p class="subhead">Get free articles, research summaries and ideas about working with kids and young people in tough times straight to your inbox</p>

  <div class="intro">
    <p class="indent">Compiled and written once a fortnight by Marla Quennell, clinical psychologist who has specialised in working with young people for the last 20 years.</p>
    <p>Past topics include: In Defence of Helicopter Parenting, What You Must ask Teens about Sexting, Teens with Strong Emotions, “Mum: Why do Teachers Hate Boys”, The Four Lessons Teens learn in Tough Times and many, many more.</p>
    <p class="quote">“These emails are gold! Thanks for sharing your wisdom” - Dana Whitcombe, Curriculum Director Riverbend College</p>
    <p>Go to <strong>www.brightpathsmind.net.au</strong> and sign up to get two free reports about kids and teens.</p>
  </div>

  <section class="panel panel-book">
    <div class="cover cover-life" role="img" aria-label="Book cover of When Life Bites: a crowd of yellow smiley balls with one sad blue ball"></div>
    <div class="copy">
      <h2>Know a teen who needs support?</h2>
      <p class="lead"><strong>WHEN LIFE BITES: IDEAS AND TACTICS FOR TEENS IN TOUGH TIMES</strong> is a primer for for Australian teens in difficult times and situations. Inside are the most common “life bites” scenarios including “My boy/girlfriend cheated on me”, “I can’t motivate myself to do any homework and I’m really behind”, “I drank too much last night”, “I feel really down and I don’t know why” and 30 more. For each scenario there is a real life story, ideas about what TO do, what NOT to do and things to tell yourself. This is the perfect book for teens to have on hand throughout adolescence and helpful for parents, teachers and those who work with teens who don’t always know what to say.</p>
      <p>Available as an ebook or hard copy from <strong>www.brightpathsmind.net.au</strong></p>
      <p class="ps">P.S. I’ve made this book as an ebook available for FREE for teenagers who can’t afford it.</p>
    </div>
  </section>

  <section class="panel panel-senior">
    <div class="copy">
      <h2>Parents, teachers and other caregivers concerns about teens in senior school are usually:</h2>
      <p>a) the teens’ stress levels, b) how much sleep teens are getting, c) how much time teens spend on quirlo/gaming, and d) teens leaving assignments till the last minute or not doing them at all.</p>
      <p>Having talked to and worked with thousands of Australian teens in schools over the last 15 years, Clinical Psychologist, Marla Quennell has written this book for parents, teachers and caregivers to help them know how to support teenagers in Years 10, 11 and 12. It includes real life stories and sections on: communicating with quiet teens, reducing conflict, parties and the formal, schoolies, drugs and alcohol, helping teens who stress out and helping teens motivate themselves. More importantly: there are cartoons!</p>
      <p class="avail">Available via ebook or in hard copy from <strong>www.brightpathsmind.net.au</strong></p>
    </div>
    <div class="cover cover-years" role="img" aria-label="Book cover of The Years That Shape Us: dark blue cover with a laptop, phone and sticky notes"></div>
  </section>

</div>
</body>
</html>
```